BrightLedgerMoney(.com) needs website & logo design

We need our website mock-up made into a reality! We are wanting to launch a multifaceted website for all things financial - i.e. blogs, financial wellness information, and a network of redirect links.
We have an existing mock-up, which I will include, but are open to your creative approach!

Industry/Entity Type

Finance

Coding

Coded - Design and coding required

Number of Pages Required

1 page

Requirements
Must have
• Corresponding logo

```html
<!DOCTYPE html>
<html lang="en">
<head>
<meta charset="utf-8">
<title>Bright Ledger Money</title>
<link href="https://fonts.googleapis.com/css2?family=Montserrat:wght@500;600;700;800&family=Lato:wght@400;700&display=swap" rel="stylesheet">
<style>
:root{
  --green:#1b8a22;
  --green-dark:#032a06;
  --green-deep:#1e4a2a;
  --green-soft:#d3fdd2;
  --ink:#111;
  --text:#444;
  --grey-bg:#f3f3f3;
  --white:#fff;
}
*{margin:0;padding:0;box-sizing:border-box}
html,body{width:1200px;height:3809px;overflow:hidden}
body{position:relative;background:var(--white);font-family:"Lato",sans-serif;color:var(--text)}
.section{position:absolute;left:0;width:1200px}
h1,h2,h3,.btn,.brand,.nav,.feature-label,.card-label{font-family:"Montserrat",sans-serif}
.btn{display:inline-flex;align-items:center;justify-content:center;font-weight:700;font-size:15px;border-radius:6px;text-decoration:none}

/* hero */
.hero{top:0;height:724px;overflow:hidden}
.hero-art{position:absolute;inset:0;background:
  radial-gradient(ellipse 380px 300px at 640px 480px,#4fd45c 0%,rgba(79,212,92,0) 70%),
  linear-gradient(180deg,#e6fbe3 0%,#c2f2bc 35%,#8fe38a 70%,#6fd86b 100%)}
.header{position:absolute;top:0;left:0;width:1200px;height:110px}
.brand{position:absolute;left:126px;top:40px;font-size:22px;font-weight:700;color:var(--ink);letter-spacing:.5px}
.nav{position:absolute;right:108px;top:46px;display:flex;gap:48px;font-size:14px;font-weight:500;color:#222;font-family:"Lato",sans-serif}
.hero-copy{position:absolute;top:155px;left:0;width:1200px;text-align:center}
.hero-copy h1{font-size:44px;font-weight:700;color:var(--ink);letter-spacing:.5px}
.hero-copy h1 span{color:var(--green)}
.hero-copy h3{margin-top:24px;font-size:18px;font-weight:700;color:var(--ink)}
.hero-copy p{margin:8px auto 0;width:500px;font-size:14.5px;line-height:26px;color:#333}
.hero .btn{margin-top:22px;width:166px;height:52px;background:var(--green-dark);color:#fff;font-size:14px}

/* feature band */
.features{top:724px;height:191px;background:var(--green-dark);display:flex;justify-content:center;align-items:center}
.feature{display:flex;flex-direction:column;align-items:center;justify-content:center;gap:10px;padding:0 38px;border-right:2px solid #fff;height:68px}
.feature:last-child{border-right:none}
.feature svg{width:42px;height:42px;stroke:#fff;fill:none;stroke-width:2}
.feature-label{color:#fff;font-weight:700;font-size:18px}

/* trending */
.trending{top:915px;height:600px}
.trend-accent{position:absolute;left:288px;top:238px;width:356px;height:272px}
.trend-photo{position:absolute;left:111px;top:96px;width:513px;height:398px;background:linear-gradient(135deg,#d8d6cf 0%,#9d8f7c 45%,#4a3a36 100%)}
.trend-text{position:absolute;left:684px;top:98px;width:410px}
.trend-text h2{font-size:35px;line-height:46px;font-weight:700;color:var(--ink)}
.trend-text p{margin-top:22px;font-size:15.5px;line-height:25.7px;color:#444}
.trend-text .btn{margin-top:28px;width:167px;height:53px;background:var(--green);color:#fff}

/* topics */
.topics{top:1515px;height:602px;background:var(--grey-bg)}
.topic-grid{position:absolute;left:167px;top:99px;display:grid;grid-template-columns:repeat(3,259px);column-gap:45px;row-gap:40px}
.topic{position:relative;height:183px;background:#fff;border-radius:8px;overflow:hidden;box-shadow:0 4px 14px rgba(0,0,0,.06)}
.topic .dome{position:absolute;left:24px;top:-104px;width:210px;height:208px;border-radius:50%;background:var(--green-soft)}
.topic.active .dome{background:var(--green)}
.topic svg{position:absolute;left:104px;top:20px;width:52px;height:52px;fill:none;stroke:#111;stroke-width:1.8}
.topic.active svg{stroke:#fff}
.card-label{position:absolute;left:0;right:0;bottom:0;height:100px;display:flex;align-items:center;justify-content:center;text-align:center;font-size:20px;font-weight:600;color:var(--ink);line-height:30px;padding-top:12px}

/* wellness */
.wellness{top:2117px;height:360px;display:flex;justify-content:space-between}
.panel{width:594px;height:360px;text-align:center;color:#fff;padding-top:50px}
.panel.light{background:linear-gradient(120deg,#2aa23a 0%,#1f8f2e 60%,#2d9a3b 100%)}
.panel.dark{width:597px;background:linear-gradient(120deg,#2b5a33 0%,#1b3f24 55%,#23462a 100%)}
.panel h2{font-size:32px;font-weight:700;letter-spacing:.5px}
.panel p{margin:18px auto 0;width:450px;font-size:14.5px;line-height:28.5px}
.panel .btn{margin-top:28px;width:167px;height:53px;background:#fff;color:var(--green);font-size:14px}

/* blog */
.blog{top:2477px;height:713px}
.blog h2{position:absolute;top:76px;width:100%;text-align:center;font-size:35px;font-weight:700;color:var(--ink)}
.post{position:absolute;top:168px;width:307px;height:451px}
.post .body{position:absolute;left:0;top:119px;width:307px;height:332px;background:#fff;border-radius:30px;box-shadow:0 6px 20px rgba(0,0,0,.08)}
.post .photo{position:absolute;left:16px;top:0;width:275px;height:236px;border-radius:37px}
.post .date{position:absolute;left:32px;top:16px;height:30px;padding:0 20px;border-radius:15px;background:var(--green);color:#fff;font-size:13px;display:flex;align-items:center}
.post h3{position:absolute;top:268px;left:10px;right:10px;text-align:center;font-size:21.5px;line-height:30px;font-weight:700;color:var(--ink)}
.post p{position:absolute;top:340px;left:14px;right:14px;text-align:center;font-size:14.5px;line-height:26px}
.post .more{position:absolute;top:394px;left:0;right:0;text-align:center;font-family:"Montserrat",sans-serif;font-weight:700;font-size:15px;color:var(--green)}
.post .more svg{vertical-align:middle;margin-left:2px}

/* newsletter + footer */
.bottom{top:3190px;height:619px;background:var(--grey-bg)}
.bottom h2{position:absolute;top:54px;width:100%;text-align:center;font-size:35px;font-weight:700;color:var(--ink)}
.signup{position:absolute;left:236px;top:129px;display:flex;gap:16px}
.signup .field{width:543px;height:54px;border-radius:27px;background:#e6e6e6;display:flex;align-items:center;padding-left:32px;font-size:16px;color:#444}
.signup .btn{width:180px;height:54px;border-radius:27px;background:var(--green);color:#fff;font-size:16px}
.rule{position:absolute;left:111px;width:980px;height:1px;background:#d8d8d8}
.foot-brand{position:absolute;left:113px;top:310px;width:290px;font-family:"Montserrat",sans-serif;font-weight:700;font-size:30px;line-height:40px;color:var(--ink)}
.foot-col{position:absolute;top:307px}
.foot-col h4{font-family:"Montserrat",sans-serif;font-size:16.5px;font-weight:700;color:var(--ink);margin-bottom:14px}
.foot-col li{list-style:none;font-size:15px;color:#333;line-height:31px;display:flex;align-items:center;gap:8px}
.foot-col li svg{width:13px;height:13px;fill:#111}
.social{display:flex;gap:10px;margin-top:8px}
.social span{width:26px;height:26px;border-radius:50%;background:#ddd}
.social span:first-child{width:30px;height:30px;background:var(--green)}
.copyright{position:absolute;top:540px;width:100%;text-align:center;font-size:15px;color:#333}
.copyright a{color:var(--green);text-decoration:underline}
</style>
</head>
<body>

<section class="section hero">
  <div class="hero-art" role="img" aria-label="Large green 3D dollar sign rising from a gridded landscape with a businesswoman standing beside it"></div>
  <header class="header">
    <div class="brand">BRIGHT LEDGER MONEY</div>
    <nav class="nav"><span>Home</span><span>About Us</span><span>Our Services</span><span>Testimonial</span><span>Contact Us</span></nav>
  </header>
  <div class="hero-copy">
    <h1>BRIGHT LEDGER <span>MONEY</span></h1>
    <h3>Trending in 2021 Financial literacy</h3>
    <p>Having insight to relevant infomation is what we bring to the table in a clear and easy to digest way.</p>
    <a class="btn" href="#">GET STARTED</a>
  </div>
</section>

<section class="section features">
  <div class="feature"><svg viewBox="0 0 42 42"><circle cx="18" cy="18" r="9" stroke-width="4"/><path d="M25 25l8 8" stroke-width="5" stroke-linecap="round"/></svg><span class="feature-label">SAVE</span></div>
  <div class="feature"><svg viewBox="0 0 42 42"><rect x="20" y="16" width="16" height="20" rx="2"/><path d="M23 22h10M23 27h10M23 32h10"/><circle cx="13" cy="26" r="8"/><path d="M13 21v10M10 23h5M10 29h5"/><path d="M10 12l3-5 3 5z"/></svg><span class="feature-label">BUDGET</span></div>
  <div class="feature"><svg viewBox="0 0 42 42"><rect x="10" y="5" width="22" height="32" rx="3"/><rect x="14" y="9" width="14" height="6"/><path d="M14 20h4v4h-4zM20 20h4v4h-4zM26 20h2v4h-2zM14 27h4v4h-4zM20 27h4v4h-4zM26 27h2v4h-2z"/></svg><span class="feature-label">CALCULATE</span></div>
  <div class="feature"><svg viewBox="0 0 42 42"><path d="M12 20c-4-5-6-8-6-11a6 6 0 0 1 12 0c0 3-2 6-6 11z"/><circle cx="12" cy="9" r="2"/><rect x="14" y="22" width="16" height="10"/><path d="M30 25h6l3 4v3h-9z"/><circle cx="19" cy="34" r="2.5"/><circle cx="34" cy="34" r="2.5"/></svg><span class="feature-label">TRACK</span></div>
  <div class="feature"><svg viewBox="0 0 42 42"><circle cx="14" cy="14" r="7"/><circle cx="14" cy="14" r="3"/><circle cx="22" cy="24" r="8"/><path d="M28 30l7 7" stroke-width="4" stroke-linecap="round"/><path d="M19 24h6"/></svg><span class="feature-label">RESEARCH</span></div>
  <div class="feature"><svg viewBox="0 0 42 42"><circle cx="22" cy="15" r="8"/><path d="M22 10v10M19 12h5M19 18h5"/><path d="M4 32h8l8 3 14-7-3-2-10 4h-7"/><path d="M22 2v3"/></svg><span class="feature-label">INVEST</span></div>
</section>

<section class="section trending">
  <svg class="trend-accent" viewBox="0 0 356 272"><polygon points="356,0 356,272 0,272" fill="#1b8a22"/></svg>
  <div class="trend-photo" role="img" aria-label="Three colleagues in an office reviewing financial documents around a laptop"></div>
  <div class="trend-text">
    <h2>TRENDING IN 2021 FINANCIAL LITERACY</h2>
    <p>Lorem ipsum dolor sit amet, consectetur adipiscing elit, sed do eiusmod tempor incididunt ut labore et dolore magna aliqua. Quis ipsum suspendisse ultrices gravida. Risus commodo viverra maecenas accumsan lacus vel facilisis.&nbsp; Lorem ipsum dolor sit amet, consectetur adipiscing elit, sed do eiusmod tempor incididunt ut labore et dolore magna aliqua. Quis ipsum suspendisse ultrices gravida. Risus commodo viverra maecenas accumsan lacus vel facilisis.</p>
    <a class="btn" href="#">LEARN MORE</a>
  </div>
</section>

<section class="section topics">
  <div class="topic-grid">
    <div class="topic"><div class="dome"></div><svg viewBox="0 0 52 52"><rect x="6" y="4" width="26" height="38" rx="2"/><path d="M11 12h4v4h-4zM19 14h9M11 22h4v4h-4zM19 24h9M11 32h4v4h-4z"/><circle cx="38" cy="36" r="9"/><circle cx="38" cy="36" r="4"/><path d="M38 36l10-10"/></svg><div class="card-label">SET GOALS</div></div>
    <div class="topic active"><div class="dome"></div><svg viewBox="0 0 52 52"><path d="M28 16c-8 6-12 14-10 22 2 6 18 6 20 0 2-8-2-16-10-22z"/><path d="M24 10l4 6 4-6z"/><path d="M28 24v12M25 27h5M25 33h5"/><rect x="6" y="28" width="10" height="5"/><rect x="6" y="34" width="10" height="5"/><rect x="6" y="40" width="10" height="5"/></svg><div class="card-label">MONEY 101</div></div>
    <div class="topic"><div class="dome"></div><svg viewBox="0 0 52 52"><rect x="16" y="6" width="20" height="38" rx="2"/><rect x="24" y="18" width="20" height="26" rx="2"/><path d="M28 23h12M28 29h4v4h-4zM35 29h4v4h-4zM28 36h4v4h-4zM35 36h4v4h-4z"/><circle cx="12" cy="38" r="6"/><path d="M20 12h10"/></svg><div class="card-label">BUDGETING</div></div>
    <div class="topic"><div class="dome"></div><svg viewBox="0 0 52 52"><path d="M6 26l16-18 22 20-16 18z"/><path d="M12 20l22 20"/><rect x="18" y="26" width="28" height="18" rx="2"/><path d="M22 38h6M32 36h10"/></svg><div class="card-label">CREDIT<br>MINDFULNESS</div></div>
    <div class="topic"><div class="dome"></div><svg viewBox="0 0 52 52"><circle cx="20" cy="20" r="14"/><path d="M20 6v14h14"/><rect x="24" y="28" width="22" height="16"/><path d="M28 28v-6h14v6"/><text x="27" y="40" font-size="8" font-family="Montserrat, sans-serif" stroke="none" fill="#111">DEBT</text></svg><div class="card-label">DEBT MANAGEMENT</div></div>
    <div class="topic"><div class="dome"></div><svg viewBox="0 0 52 52"><rect x="6" y="10" width="36" height="30" rx="3"/><path d="M6 18h36M14 6v8M34 6v8M11 23h5v4h-5zM19 23h5v4h-5zM27 23h5v4h-5zM11 31h5v4h-5zM19 31h5v4h-5z"/><circle cx="40" cy="38" r="7"/></svg><div class="card-label">RETIREMENT<br>PLANNING</div></div>
  </div>
</section>

<section class="section wellness">
  <div class="panel light" role="img" aria-label="Green tinted photo of a person reviewing finances">
    <h2>FINANCIAL WELLNESS 101</h2>
    <p>Lorem ipsum dolor sit amet, consectetur adipiscing elit, sed do eiusmod tempor incididunt ut labore et dolore magna aliqua. Quis ipsum suspendisse ultrices gravida. Risus commodo viverra maecenas accumsan lacus vel facilisis.</p>
    <a class="btn" href="#">LEARN MORE</a>
  </div>
  <div class="panel dark" role="img" aria-label="Dark green tinted photo of a desk with plants and paperwork">
    <h2>FINANCIAL WELLNESS 101</h2>
    <p>Lorem ipsum dolor sit amet, consectetur adipiscing elit, sed do eiusmod tempor incididunt ut labore et dolore magna aliqua. Quis ipsum suspendisse ultrices gravida. Risus commodo viverra maecenas accumsan lacus vel facilisis.</p>
    <a class="btn" href="#">CONTACT US</a>
  </div>
</section>

<section class="section blog">
  <h2>OUR BLOG</h2>
  <article class="post" style="left:111px">
    <div class="body"></div>
    <div class="photo" role="img" aria-label="Calculator, stacked coins and a piggy bank on a desk" style="background:linear-gradient(135deg,#e8d3a8 0%,#b8976a 50%,#5a4530 100%)"></div>
    <span class="date">Mar 23, 2023</span>
    <h3>Lorem ipsum dolor sit amet, consectetur</h3>
    <p>Lorem ipsum dolor sit amet, consectetur adipiscing elit</p>
    <div class="more">Learn More<svg width="22" height="14" viewBox="0 0 22 14"><circle cx="8" cy="7" r="6" fill="#9fd99f"/><path d="M4 7h14M14 3l4 4-4 4" stroke="#1b8a22" stroke-width="2" fill="none"/></svg></div>
  </article>
  <article class="post" style="left:446px">
    <div class="body"></div>
    <div class="photo" role="img" aria-label="Coin stacks in front of a falling red market chart" style="background:linear-gradient(135deg,#2b2b2b 0%,#5a3a2a 45%,#c08a4a 75%,#1e1e1e 100%)"></div>
    <span class="date">Mar 23, 2023</span>
    <h3>Lorem ipsum dolor sit amet, consectetur</h3>
    <p>Lorem ipsum dolor sit amet, consectetur adipiscing elit</p>
    <div class="more">Learn More<svg width="22" height="14" viewBox="0 0 22 14"><circle cx="8" cy="7" r="6" fill="#9fd99f"/><path d="M4 7h14M14 3l4 4-4 4" stroke="#1b8a22" stroke-width="2" fill="none"/></svg></div>
  </article>
  <article class="post" style="left:781px">
    <div class="body"></div>
    <div class="photo" role="img" aria-label="Hands writing notes beside a tablet showing charts" style="background:linear-gradient(135deg,#d9dde2 0%,#a6a29a 45%,#5a4a3e 100%)"></div>
    <span class="date">Mar 23, 2023</span>
    <h3>Lorem ipsum dolor sit amet, consectetur</h3>
    <p>Lorem ipsum dolor sit amet, consectetur adipiscing elit</p>
    <div class="more">Learn More<svg width="22" height="14" viewBox="0 0 22 14"><circle cx="8" cy="7" r="6" fill="#9fd99f"/><path d="M4 7h14M14 3l4 4-4 4" stroke="#1b8a22" stroke-width="2" fill="none"/></svg></div>
  </article>
</section>

<section class="section bottom">
  <h2>STAY INFORMED WITH OUR LATEST NEWS</h2>
  <div class="signup"><div class="field">Enter Your Email</div><a class="btn" href="#">SUBSCRIBE</a></div>
  <div class="rule" style="top:242px"></div>
  <div class="foot-brand">BRIGHT LEDGER<br>MONEY</div>
  <div class="foot-col" style="left:436px">
    <h4>CONTACT INFO</h4>
    <ul>
      <li><svg viewBox="0 0 12 14"><path d="M6 0a5 5 0 0 0-5 5c0 4 5 9 5 9s5-5 5-9a5 5 0 0 0-5-5zm0 7a2 2 0 1 1 0-4 2 2 0 0 1 0 4z"/></svg>Sed ut perspiciatis unde omnis</li>
      <li><svg viewBox="0 0 14 14"><path d="M3 0l3 3-2 2c1 2 3 4 5 5l2-2 3 3-2 3C6 14 0 8 0 2z"/></svg>+(123) 456-7890</li>
      <li><svg viewBox="0 0 14 12" fill="none"><rect x="1" y="1" width="12" height="10" fill="none" stroke="#111" stroke-width="1.4"/><path d="M1 1l6 5 6-5" fill="none" stroke="#111" stroke-width="1.4"/></svg>Email:hello@brightledgermoney.com</li>
    </ul>
  </div>
  <div class="foot-col" style="left:720px">
    <h4>CUSTOMER SERVICE</h4>
    <ul><li>Terms &amp; conditions</li><li>Privacy Policy</li><li>About Us</li><li>Support</li></ul>
  </div>
  <div class="foot-col" style="left:941px">
    <h4>FOLLOW US</h4>
    <div class="social"><span></span><span></span><span></span><span></span></div>
  </div>
  <div class="rule" style="top:500px"></div>
  <div class="copyright">©Copyrights 2023 <a href="#">Bright Ledger Money</a> &nbsp;|&nbsp;&nbsp; All Rights Reserved</div>
</section>

</body>
</html>
```